Design My Bussiness Card
Technology company
Project: Design My Bussiness Card
Design My Bussiness Card -
Creative Brief
Professional
Dorian Pelkey
2847 E. Tollbrook #3
marisa@vantrelo.net
www.qoribelix.info

```html
<!DOCTYPE html>
<html lang="en">
<head>
<meta charset="utf-8">
<title>Qoribelix Stationery</title>
<link rel="stylesheet" href="https://fonts.googleapis.com/css2?family=Open+Sans:wght@400;600;700&display=swap">
<style>
  :root {
    --green-dark: #0b7a3b;
    --green: #1f9a4c;
    --green-light: #8ccf9c;
    --green-faint: #e3f2e6;
    --ink: #555a5e;
    --ink-dark: #3f4448;
    --paper: #ffffff;
    --board: #ffffff;
    --line: #dcdcdc;
  }
  * { margin: 0; padding: 0; box-sizing: border-box; }
  html, body { width: 1200px; height: 713px; overflow: hidden; background: #f4f4f4; }
  body { position: relative; font-family: "Open Sans", Arial, sans-serif; color: var(--ink); }

  .board {
    position: absolute; left: 19px; top: 19px; width: 1162px; height: 675px;
    background: var(--board); border: 1px solid var(--line); border-radius: 6px;
    box-shadow: 0 2px 8px rgba(0,0,0,.12);
  }
  .sheet {
    position: absolute; background: var(--paper); overflow: hidden;
    box-shadow: 0 1px 4px rgba(0,0,0,.22);
  }

  .card-front { left: 67px; top: 43px; width: 331px; height: 197px; }
  .card-back {
    left: 67px; top: 247px; width: 331px; height: 197px;
    background: radial-gradient(ellipse at 50% 35%, #e8f5ea 0%, #9fd5ac 55%, #3fae60 100%);
  }
  .letterhead { left: 422px; top: 48px; width: 418px; height: 624px; }
  .envelope { left: 576px; top: 173px; width: 564px; height: 223px; }

  .swoosh { position: absolute; left: 0; top: 0; }

  .person-name { position: absolute; color: var(--green); font-size: 15px; font-weight: 400; }
  .card-front .person-name { left: 160px; top: 22px; }
  .letterhead .person-name { right: 34px; top: 58px; font-size: 16px; }

  .contact { position: absolute; list-style: none; font-size: 8.5px; line-height: 12px; color: var(--ink); }
  .contact b { display: inline-block; width: 14px; color: var(--green-dark); font-weight: 700; }
  .card-front .contact { left: 154px; top: 122px; }
  .letterhead .contact { left: 62px; top: 540px; }
  .envelope .contact { left: 50px; top: 134px; }

  .brand { position: absolute; display: flex; align-items: center; gap: 8px; }
  .brand-dot { width: 30px; height: 30px; border-radius: 50%; background: var(--green); flex: none; }
  .brand-name { font-size: 24px; font-weight: 700; color: var(--ink-dark); letter-spacing: .5px; }
  .tagline {
    position: absolute; font-size: 7px; font-weight: 600; letter-spacing: .6px;
    text-transform: uppercase; color: var(--green);
  }
  .letterhead .brand { left: 46px; top: 54px; }
  .letterhead .tagline { left: 84px; top: 86px; }
  .envelope .brand { left: 40px; top: 26px; }
  .envelope .tagline { left: 78px; top: 58px; }

  .card-back .brand { left: 50%; top: 62px; transform: translateX(-50%); flex-direction: column; gap: 6px; }
  .card-back .brand-dot { width: 42px; height: 42px; background: var(--green-dark); }
  .card-back .brand-name { color: var(--green-dark); font-size: 20px; }
  .card-back .tagline { left: 0; right: 0; top: 150px; text-align: center; color: #fff; font-size: 8px; }
  .card-back .web { position: absolute; left: 0; right: 0; top: 164px; text-align: center; color: #fff; font-size: 9px; font-weight: 600; }

  .faint-mark { position: absolute; border-radius: 50%; background: var(--green-faint); }
  .letterhead .faint-mark { left: 312px; top: 496px; width: 96px; height: 96px; }
  .envelope .faint-mark { left: 436px; top: 92px; width: 116px; height: 116px; }
</style>
</head>
<body>
  <div class="board"></div>

  <section class="sheet card-front">
    <svg class="swoosh" width="331" height="197" viewBox="0 0 331 197">
      <defs>
        <linearGradient id="frontGreen" x1="0" y1="0" x2="1" y2="1">
          <stop offset="0" stop-color="#0b7a3b"/>
          <stop offset="1" stop-color="#3fae60"/>
        </linearGradient>
      </defs>
      <path d="M0 0 H96 C60 40 34 110 0 197 Z" fill="url(#frontGreen)"/>
      <path d="M104 0 C66 44 40 116 8 197" fill="none" stroke="#8ccf9c" stroke-width="2"/>
    </svg>
    <h2 class="person-name">Dorian Pelkey</h2>
    <ul class="contact">
      <li><b>P</b>5550142087</li>
      <li><b>F</b>5550142088</li>
      <li><b>E</b>marisa@vantrelo.net</li>
      <li><b>W</b>www.qoribelix.info</li>
    </ul>
  </section>

  <section class="sheet card-back">
    <div class="brand"><span class="brand-dot"></span><span class="brand-name">Qoribelix</span></div>
    <p class="tagline">Professional Business Services</p>
    <p class="web">www.qoribelix.info</p>
  </section>

  <section class="sheet letterhead">
    <svg class="swoosh" width="418" height="624" viewBox="0 0 418 624">
      <path d="M0 0 H70 C40 14 26 40 24 80 V624 H0 Z" fill="#0b7a3b"/>
      <path d="M78 0 C46 16 32 42 30 84 V624" fill="none" stroke="#8ccf9c" stroke-width="2"/>
    </svg>
    <div class="brand"><span class="brand-dot"></span><span class="brand-name">Qoribelix</span></div>
    <p class="tagline">Professional Business Services</p>
    <h2 class="person-name">Dorian Pelkey</h2>
    <ul class="contact">
      <li><b>P</b>5550142087</li>
      <li><b>F</b>5550142088</li>
      <li><b>E</b>marisa@vantrelo.net</li>
      <li><b>W</b>www.qoribelix.info</li>
    </ul>
    <div class="faint-mark"></div>
  </section>

  <section class="sheet envelope">
    <svg class="swoosh" width="564" height="223" viewBox="0 0 564 223">
      <rect x="0" y="0" width="14" height="223" fill="#0b7a3b"/>
      <line x1="19" y1="0" x2="19" y2="223" stroke="#8ccf9c" stroke-width="2"/>
    </svg>
    <div class="brand"><span class="brand-dot"></span><span class="brand-name">Qoribelix</span></div>
    <p class="tagline">Professional Business Services</p>
    <ul class="contact">
      <li><b>P</b>5550142087</li>
      <li><b>F</b>5550142088</li>
      <li><b>E</b>marisa@vantrelo.net</li>
      <li><b>W</b>www.qoribelix.info</li>
    </ul>
    <div class="faint-mark"></div>
  </section>
</body>
</html>
```